Brimlock Assurance Branding Revamp

We are a consulting company, looking for a way to display and promote our brand. We have 2 sides to the business- Brimlock (financial) and Assurance (cyber security). The financial side products relate to business necessities: card processing, website design/hosting/maintenance, VoIP phone systems. The cyber security side promotes a bundled package of 4 solutions: network vulnerability scan, dark web scan, anti-ransomeware/malware software, and image-level backups. We want people to understand that partnering with Brimlock Assurance gives them “Elevated Peace of Mind” (tagline). Current badge and logos uploaded.

Target Market(s)

Small businesses

Contact Information for Business Card

Carla Whitfield, Vice President, carla@brimlockassurance.example, 555-384-9106, www.brimlockassurance.example

Requirements
Nice to have
• I do prefer the darker background for front and back

```html
<!DOCTYPE html>
<html lang="en">
<head>
<meta charset="utf-8">
<title>Brimlock Assurance – Business Card</title>
<link rel="stylesheet" href="https://fonts.googleapis.com/css2?family=Poppins:wght@400;500;600&display=swap">
<style>
  :root {
    --page: #ffffff;
    --card: #1f1e1d;
    --card-light: #2b2a28;
    --white: #ffffff;
    --red: #e0202a;
    --red-deep: #7d0509;
    --ink: #111111;
  }
  * { margin: 0; padding: 0; box-sizing: border-box; }
  html, body { width: 1200px; height: 848px; overflow: hidden; background: var(--page); }
  body { position: relative; font-family: "Poppins", sans-serif; color: var(--white); }

  .card {
    position: absolute;
    width: 493px; height: 282px;
    background: var(--card);
    overflow: hidden;
  }
  .card--front { left: 97px; top: 137px;
    background: linear-gradient(115deg, var(--card) 45%, var(--card-light) 75%, var(--card) 100%); }
  .card--back { left: 610px; top: 430px; }

  .side-label {
    position: absolute;
    font-size: 23px; color: var(--ink); font-weight: 400;
    transform: translateX(-50%);
    white-space: nowrap;
  }
  .side-label--front { left: 337px; top: 434px; }
  .side-label--back { left: 856px; top: 386px; }

  /* front */
  .brand {
    position: absolute; left: 10px; top: 92px; width: 200px;
    display: flex; align-items: center; gap: 10px; justify-content: center;
  }
  .brand__mark { width: 14px; height: 14px; background: var(--red); flex: none; }
  .brand__name {
    font-size: 16px; font-weight: 500; letter-spacing: 3px; line-height: 1.3;
    text-transform: uppercase; color: var(--white); white-space: nowrap;
  }

  .address-band {
    position: absolute; left: 0; top: 207px; width: 305px; height: 75px;
    background: linear-gradient(90deg, var(--red) 0%, var(--red-deep) 70%, var(--card) 100%);
    clip-path: polygon(0 0, 260px 0, 305px 75px, 0 75px);
  }
  .address {
    position: absolute; left: 20px; top: 213px;
    font-size: 8.5px; font-weight: 500; letter-spacing: 1.4px; line-height: 18.5px;
    list-style: none; white-space: nowrap;
  }

  .divider { position: absolute; left: 287px; top: 102px; width: 2px; height: 94px; background: var(--red); }
  .contact { position: absolute; left: 299px; top: 98px; width: 186px; }
  .contact__name { font-size: 15px; font-weight: 400; letter-spacing: 1.6px; line-height: 1.2; white-space: nowrap; }
  .contact__title { font-size: 11.5px; letter-spacing: 1.4px; line-height: 1.3; white-space: nowrap; }
  .contact__row {
    display: flex; align-items: center; gap: 6px; white-space: nowrap;
  }
  .contact__row--phone { margin-top: 14px; font-size: 12px; letter-spacing: 2px; }
  .contact__row--email { margin-top: 14px; font-size: 8.2px; letter-spacing: 0.4px; }
  .icon { width: 12px; height: 12px; flex: none; }

  /* back */
  .back-brand {
    position: absolute; left: 0; right: 0; top: 100px;
    display: flex; align-items: center; justify-content: center; gap: 12px;
  }
  .back-brand .brand__mark { width: 18px; height: 18px; }
  .back-brand .brand__name { font-size: 22px; letter-spacing: 4px; }
  .website {
    position: absolute; left: 0; right: 0; top: 246px; text-align: center;
    font-size: 12px; letter-spacing: 1.6px; white-space: nowrap;
  }
</style>
</head>
<body>
  <section class="card card--front" aria-label="Business card front">
    <div class="brand">
      <span class="brand__mark"></span>
      <span class="brand__name">Brimlock<br>Assurance</span>
    </div>

    <div class="address-band"></div>
    <ul class="address">
      <li>42 Harlow Lane</li>
      <li>Millbrook, Los Angeles, 90017</li>
      <li>USA</li>
    </ul>

    <div class="divider"></div>
    <div class="contact">
      <p class="contact__name">Carla Whitfield</p>
      <p class="contact__title">Vice President</p>
      <p class="contact__row contact__row--phone">
        <svg class="icon" viewBox="0 0 24 24" aria-hidden="true"><path fill="#e0202a" d="M6.6 2.5l3 4.2-2 2.3c1.2 2.7 3.4 5 6.1 6.3l2.3-2 4.2 3-1.7 4.2C10.6 20.6 3.4 13.4 2.5 5.5z"/></svg>
        555-384-9106
      </p>
      <p class="contact__row contact__row--email">
        <svg class="icon" viewBox="0 0 24 24" aria-hidden="true"><rect x="2" y="5" width="20" height="14" fill="none" stroke="#e0202a" stroke-width="1.6"/><path d="M2 5l10 8 10-8" fill="none" stroke="#e0202a" stroke-width="1.6"/></svg>
        carla@brimlockassurance.example
      </p>
    </div>
  </section>
  <p class="side-label side-label--front">Front</p>

  <p class="side-label side-label--back">Back</p>
  <section class="card card--back" aria-label="Business card back">
    <div class="back-brand">
      <span class="brand__mark"></span>
      <span class="brand__name">Brimlock Assurance</span>
    </div>
    <p class="website">www.brimlockassurance.example</p>
  </section>
</body>
</html>
```